43 Year Old Construction firm needs Updated Business Card & Stationery Design

We are an established and well known (in our market) commercial construction firm. We need a cleaner and more modern look for our corporate identity material. We would like to continue to use our current colors and logo.
We are thinking about incorporating a slogan on our business card (either front or back): "Striving to be the most trusted builder in our market." The text could change at some point. Our website is www.kradworth.example . Sample card is attached. Some will have more phone numbers, etc...
Updates

Target Market(s)

Commercial and institutional clients.

Industry/Entity Type

Construction Company

Contact Information for Business Card

See attached for existing card. But don't be constrained.

Requirements
Must have
• Logo, name, title, address, website, email, phone numbers (as few as one, as many as three)
• Slogan on front or back "Striving to be the most trusted builder in our market"
• Use existing logo and colors

```html
<!DOCTYPE html>
<html lang="en">
<head>
<meta charset="utf-8">
<title>Kradworth Constructors – Business Card</title>
<link rel="stylesheet" href="https://fonts.googleapis.com/css2?family=Open+Sans:wght@400;600;700&display=swap">
<style>
  :root {
    --backdrop: #3a3330;
    --card-white: #f7f7f5;
    --brand-blue: #0b4a8b;
    --text-dark: #2b2b2b;
    --label-blue: #1f5fa8;
  }
  * { box-sizing: border-box; margin: 0; padding: 0; }
  html, body {
    width: 1200px; height: 844px; overflow: hidden;
    background: var(--backdrop);
    font-family: "Open Sans", Arial, sans-serif;
  }
  .canvas {
    position: relative; width: 1200px; height: 844px;
    display: flex; align-items: center; justify-content: center; gap: 60px;
  }
  .card {
    position: relative; width: 520px; height: 297px;
    box-shadow: 0 10px 24px rgba(0,0,0,.45);
    overflow: hidden;
  }
  /* Front */
  .card--front { background: var(--card-white); color: var(--text-dark); }
  .brand-mark {
    position: absolute; top: 30px; right: 30px;
    display: flex; align-items: center; gap: 10px;
  }
  .brand-mark__square { width: 22px; height: 22px; background: var(--brand-blue); }
  .brand-mark__name {
    color: var(--brand-blue); font-weight: 700; font-size: 17px;
    letter-spacing: .5px; text-transform: uppercase;
  }
  .contact {
    position: absolute; left: 34px; bottom: 30px;
    font-size: 13px; line-height: 1.45;
  }
  .contact__name { color: var(--brand-blue); font-weight: 700; font-size: 17px; line-height: 1.2; }
  .contact__title { margin-bottom: 18px; }
  .contact__address { margin-bottom: 12px; }
  .contact__row span + span { margin-left: 14px; }
  .contact__label { color: var(--label-blue); }
  .contact__web { color: var(--label-blue); }
  /* Back */
  .card--back { background: var(--brand-blue); }
  .card--back .brand-name {
    position: absolute; top: 0; left: 0; right: 0; height: 245px;
    display: flex; align-items: center; justify-content: center;
    color: #fff; font-weight: 700; font-size: 30px; letter-spacing: 2px;
    text-transform: uppercase;
  }
  .slogan-band {
    position: absolute; left: 0; right: 0; bottom: 0; height: 52px;
    background: var(--card-white);
    display: flex; align-items: center; justify-content: center;
    color: var(--brand-blue); font-weight: 600; font-size: 15px;
  }
</style>
</head>
<body>
<main class="canvas">
  <section class="card card--front" aria-label="Business card front">
    <div class="brand-mark">
      <span class="brand-mark__square"></span>
      <span class="brand-mark__name">Kradworth Constructors</span>
    </div>
    <div class="contact">
      <p class="contact__name">John Smith</p>
      <p class="contact__title">Managing Director</p>
      <p class="contact__address">1234, Address GoesHere, Country, 12345</p>
      <p class="contact__row"><span><span class="contact__label">T:</span>(044) 123 456 78</span><span><span class="contact__label">M:</span> (044)123456789</span></p>
      <p class="contact__row"><span><span class="contact__label">E:</span>info@kradworth.example</span><span class="contact__web">www.kradworth.example</span></p>
    </div>
  </section>
  <section class="card card--back" aria-label="Business card back">
    <p class="brand-name">Kradworth Constructors</p>
    <p class="slogan-band">Striving to be the most trusted builder in our market</p>
  </section>
</main>
</body>
</html>
```